Web re-design project www.vempresoft.com

We need a corporate website for a startup company called Vempre Labs. The company offers web-based worksite management system for big construction companies. In short, replacing annoying papers with iPads.
We need the site main page to provide basic overview of the company and then inner page layout for displaying news and detailed information about products.
Currently we have a site up at:
http://www.vempresoft.com/en/main
but as you can see the graphic design is a bit lacking in quality(implemented by a tech guy :)
We need you to pimp that web site design up!
There is possibility for more freelance work in the future related to our web products, slide show designs and printed marketing materials.
Our main product is LOMVI. You can find a short presentation about what it does here:
http://www.vempresoft.com/en/lomvi
Here you can find packages of images and screenshots related to our company:
https://files.plimbox.net/u/7719026/vempre_images.zip
https://files.plimbox.net/u/7719026/vempresoft%20images2.zip
Product logo svg can be found here:
https://files.plimbox.net/u/7719026/LOMVI-logo.svg
Your are not forced to use those images, but hopefully there will be something that is useful.
Hope to hear from you guys soon!
Cheers,
Ossi
Update:
We will be using LOMVI logo as the company brand. I don't like our current Vempre Labs company logo, so that doesn't need to be included in the site design.
Update 2:
I like website designs that are "light", elegant and pretty simplistic. One example is our product login page (screenshot included in files).
Update 3:
Sites from the same industry / type of products:
http://www.rakmoda.fi/
http://www.quarvelgrid.com/products/software/network-applications/fieldsync-3d
http://www.dornvex.com/construction/heavy-civil/software-solutions/Linked-Network.aspx?dtID=overview&
Target audience for the website is companies in the construction sector, and possibly corporate investors
Graphic Design

```html
<!DOCTYPE html>
<html lang="en">
<head>
<meta charset="utf-8">
<title>LOMVI – Vempre Labs</title>
<link rel="stylesheet" href="https://fonts.googleapis.com/css2?family=Arimo:wght@400;700&display=swap">
<style>
  :root {
    --page-bg: #f4f4f4;
    --ink: #111111;
    --muted: #555555;
    --accent: #d40a10;
    --accent-dark: #b8060b;
    --tab-bg: #fafafa;
    --tab-line: #9a9a9a;
    --rule: #bdbdbd;
    --arrow-bg: #8c8c8c;
    --photo-a: #6d6a62;
    --photo-b: #cfcac0;
  }
  * { box-sizing: border-box; margin: 0; padding: 0; }
  html, body { width: 1200px; height: 826px; overflow: hidden; }
  body {
    position: relative;
    font-family: "Arimo", Arial, sans-serif;
    color: var(--ink);
    background: linear-gradient(#ececec 0, var(--page-bg) 180px, #fafafa 600px, #ffffff 826px);
  }
  a { color: inherit; text-decoration: none; }

  .brand {
    position: absolute; left: 53px; top: 70px;
    font-size: 66px; font-weight: 400; letter-spacing: 1px; line-height: 1;
    color: var(--ink);
  }

  .main-nav { position: absolute; left: 688px; top: 59px; display: flex; gap: 3px; }
  .main-nav a {
    width: 109px; height: 98px; background: var(--tab-bg);
    border-bottom: 3px solid var(--tab-line);
    display: flex; align-items: center; padding-left: 13px;
    font-size: 15px; color: var(--ink);
  }
  .main-nav a.is-active { border-bottom-color: var(--accent); }

  .header-rule { position: absolute; left: 53px; top: 181px; width: 1089px; height: 10px; background: var(--rule); }

  .hero { position: absolute; left: 82px; top: 227px; width: 720px; height: 280px; overflow: hidden; }
  .hero-photo { position: absolute; inset: 0; background: linear-gradient(120deg, var(--photo-a), var(--photo-b) 55%); }
  .hero-panel { position: absolute; inset: 0; }
  .hero-copy {
    position: absolute; left: 408px; top: 44px;
    color: #fff; font-weight: 700; line-height: 1;
  }
  .hero-copy .big { font-size: 41px; }
  .hero-copy .small { font-size: 25px; }
  .hero-copy p { margin-bottom: 4px; white-space: nowrap; }

  .slide-arrow {
    position: absolute; top: 344px; width: 54px; height: 41px;
    background: var(--arrow-bg); display: flex; align-items: center; justify-content: center;
  }
  .slide-arrow.prev { left: 41px; }
  .slide-arrow.next { left: 788px; }

  .news { position: absolute; left: 870px; top: 242px; width: 255px; }
  .news-label { font-size: 15px; padding-bottom: 5px; border-bottom: 1px solid #555; }
  .news h2 { font-size: 34px; line-height: 30px; font-weight: 700; margin: 14px 0 8px; }
  .news p { font-size: 13.5px; line-height: 23px; color: #222; }
  .news .read-more { font-size: 14px; color: var(--accent); font-weight: 700; line-height: 23px; }

  .clients {
    position: absolute; left: 53px; top: 544px; width: 1087px; height: 106px;
    background: linear-gradient(90deg, #ededed, #ffffff 40%, #ffffff 60%, #ededed);
    display: flex; align-items: center;
  }
  .clients::after {
    content: ""; position: absolute; left: 200px; right: 200px; bottom: -22px; height: 16px;
    background: radial-gradient(ellipse at center, rgba(0,0,0,.28), rgba(0,0,0,0) 70%);
  }
  .clients-label {
    width: 225px; height: 100%; display: flex; align-items: center; justify-content: center;
    font-size: 21px; font-weight: 700; border-right: 2px solid #dcdcdc; background: #f0f0f0;
  }
  .client-list { flex: 1; display: flex; justify-content: space-around; align-items: center; }
  .client { font-size: 17px; font-weight: 700; color: var(--ink); display: flex; align-items: center; gap: 7px; }
  .client .mark { width: 12px; height: 12px; background: var(--ink); }

  .site-footer {
    position: absolute; left: 53px; top: 684px; width: 1089px;
    display: flex; justify-content: space-between; font-size: 13.5px;
  }
  .footer-nav { display: flex; gap: 12px; font-weight: 700; color: var(--muted); }
  .legal { color: #333; }
</style>
</head>
<body>
  <header>
    <div class="brand">LOMVI</div>
    <nav class="main-nav">
      <a href="#" class="is-active">HOME</a>
      <a href="#">PRODUCT</a>
      <a href="#">NEWS</a>
      <a href="#">CONTACT</a>
    </nav>
    <div class="header-rule"></div>
  </header>

  <section class="hero">
    <div class="hero-photo" role="img" aria-label="Photo of a hand using a tablet on top of road construction drawings"></div>
    <svg class="hero-panel" width="720" height="280" viewBox="0 0 720 280" aria-hidden="true">
      <defs>
        <linearGradient id="panelRed" x1="0" y1="0" x2="1" y2="0">
          <stop offset="0" stop-color="#c4050a"/>
          <stop offset="1" stop-color="#e00d13"/>
        </linearGradient>
      </defs>
      <polygon points="400,0 720,0 720,280 335,280" fill="url(#panelRed)"/>
    </svg>
    <div class="hero-copy">
      <p class="big">Cloud-based</p>
      <p><span class="small">service for </span><span class="big">road</span></p>
      <p class="big">construction</p>
      <p><span class="big">projects</span><span class="small"> and it's</span></p>
      <p class="small" style="margin-top:6px">going full steam</p>
    </div>
  </section>
  <a href="#" class="slide-arrow prev" aria-label="Previous slide">
    <svg width="18" height="26" viewBox="0 0 18 26"><polyline points="14,3 4,13 14,23" fill="none" stroke="#fff" stroke-width="4"/></svg>
  </a>
  <a href="#" class="slide-arrow next" aria-label="Next slide">
    <svg width="18" height="26" viewBox="0 0 18 26"><polyline points="4,3 14,13 4,23" fill="none" stroke="#fff" stroke-width="4"/></svg>
  </a>

  <aside class="news">
    <div class="news-label">News</div>
    <h2>Welcome to our new website!</h2>
    <p>Vempre Labs new website has been launched. From these pages you can find information about LOMVI cloud-based road construction service and other products from Vempre Labs.</p>
    <a href="#" class="read-more">Read more</a>
  </aside>

  <section class="clients">
    <div class="clients-label">OUR CLIENTS</div>
    <div class="client-list">
      <span class="client"><span class="mark"></span>Orbis Music</span>
      <span class="client">Halden Tracks</span>
      <span class="client">Northway</span>
      <span class="client">Cedar Nine</span>
      <span class="client">Relay Audio</span>
    </div>
  </section>

  <footer class="site-footer">
    <nav class="footer-nav">
      <a href="#">HOME</a><a href="#">PRODUCT</a><a href="#">NEWS</a><a href="#">CONTACT</a>
    </nav>
    <div class="legal">All rights reserved Privacy Policy Vemprelabs. © 2008</div>
  </footer>
</body>
</html>
```